Brantley Advisory Group provides support for renewable energy projects to utilities and suppliers

I need a professional looking business card that is both simple and elegant and unique. My clients are mostly large organizations not individuals. I am a consultant with my own company that is small but would like to give clients the impression I am larger. Smart grid, fiber optics, software, field hardware, distribution automation, substation automation, operations, energy storage/batteries, microgrids, customer service, strategy/roadmaps, conservation, Automated Metering Infrastruture (AMI or smart meters) are all areas of focus.

Target Market(s)

Utilities, suppliers, governmental agencies involved in energy. All types of energy especially natural gas and electrical. Especially renewable energy or green projects.

Contact Information for Business Card

Name - Mark Brantley Cell Phone - 425.318.2746 Email - mbrantley@brantleyag-example.com
Company - Brantley Advisory Group (logo) Title - Principal

Font styles to use
Serif
Sans Serif

Colors

Designer to choose colors to be used in the design.

Requirements
Must have
• Simple and professional and powerful.
• Unique/creative design.
Nice to have
• Utilize color scheme to accent logo colors. Maybe some geometric pattern on edge of card with color.
Should not have
• Busy, complicated, traditional

```html
<!DOCTYPE html>
<html lang="en">
<head>
<meta charset="utf-8">
<title>Brantley Advisory Group – Business Card</title>
<link rel="stylesheet" href="https://fonts.googleapis.com/css2?family=Arimo:wght@400;700&display=swap">
<style>
  :root {
    --backdrop: #e4e4e4;
    --card-white: #fbfbfb;
    --brand-blue: #2d4b8a;
    --brand-green: #6a9a46;
    --ink-light: #eef1f8;
    --divider: #ffffff;
  }
  * { margin: 0; padding: 0; box-sizing: border-box; }
  html, body {
    width: 1200px; height: 864px; overflow: hidden;
    background: var(--backdrop);
    font-family: "Arimo", Arial, sans-serif;
  }
  .canvas {
    position: relative; width: 1200px; height: 864px;
  }
  .card {
    position: absolute; left: 280px; width: 640px; height: 366px;
    background: var(--card-white);
    box-shadow: 0 4px 14px rgba(0,0,0,0.12);
    overflow: hidden;
  }
  .card--front { top: 40px; }
  .card--back { top: 450px; }

  .band-green, .band-blue { position: absolute; left: 0; width: 100%; }
  .band-green { background: var(--brand-green); }
  .band-blue {
    background: linear-gradient(160deg, #34559a 0%, var(--brand-blue) 55%, #28437c 100%);
    border-top: 3px solid var(--divider);
  }
  .card--front .band-green { top: 150px; height: 32px; }
  .card--front .band-blue  { top: 182px; bottom: 0; }
  .card--back .band-green  { top: 118px; height: 32px; }
  .card--back .band-blue   { top: 150px; bottom: 0; }

  .wordmark {
    position: absolute; left: 0; width: 100%;
    display: flex; align-items: center; justify-content: center; gap: 14px;
  }
  .card--front .wordmark { top: 74px; }
  .card--back .wordmark { top: 44px; }
  .wordmark__square {
    width: 34px; height: 34px;
    border: 3px solid var(--brand-green);
  }
  .wordmark__name {
    font-size: 30px; font-weight: 700; color: var(--brand-blue);
    letter-spacing: 0.3px;
  }

  .contact-list {
    position: absolute; left: 40px; top: 182px;
    list-style: none; color: var(--ink-light); font-size: 15px;
  }
  .contact-list li {
    display: flex; align-items: center; gap: 12px; height: 24px;
  }
  .contact-list svg { width: 14px; height: 14px; flex: none; }

  .person {
    position: absolute; right: 60px; top: 286px;
    color: var(--ink-light); font-size: 15px; line-height: 22px;
  }
  .person__name { font-weight: 700; }
</style>
</head>
<body>
<main class="canvas">

  <section class="card card--front" aria-label="Card front">
    <div class="wordmark">
      <span class="wordmark__square"></span>
      <span class="wordmark__name">Brantley Advisory Group</span>
    </div>
    <div class="band-green"></div>
    <div class="band-blue"></div>
  </section>

  <section class="card card--back" aria-label="Card back with contact details">
    <div class="wordmark">
      <span class="wordmark__square"></span>
      <span class="wordmark__name">Brantley Advisory Group</span>
    </div>
    <div class="band-green"></div>
    <div class="band-blue"></div>

    <ul class="contact-list">
      <li>
        <svg viewBox="0 0 14 14" aria-hidden="true"><rect x="3.5" y="0.8" width="7" height="12.4" rx="1.4" fill="none" stroke="#eef1f8" stroke-width="1.3"/><circle cx="7" cy="11" r="0.8" fill="#eef1f8"/></svg>
        <span>425.318.2746</span>
      </li>
      <li>
        <svg viewBox="0 0 14 14" aria-hidden="true"><g fill="none" stroke="#eef1f8" stroke-width="1.1"><circle cx="7" cy="7" r="6"/><ellipse cx="7" cy="7" rx="2.6" ry="6"/><line x1="1" y1="7" x2="13" y2="7"/></g></svg>
        <span>www.brantleyag-example.com</span>
      </li>
      <li>
        <svg viewBox="0 0 14 14" aria-hidden="true"><rect x="0.8" y="2.8" width="12.4" height="8.4" fill="none" stroke="#eef1f8" stroke-width="1.2"/><polyline points="0.8,2.8 7,7.6 13.2,2.8" fill="none" stroke="#eef1f8" stroke-width="1.2"/></svg>
        <span>mbrantley@brantleyag-example.com</span>
      </li>
    </ul>

    <div class="person">
      <p class="person__name">Mark Brantley</p>
      <p class="person__title">Principal</p>
    </div>
  </section>

</main>
</body>
</html>
```